Photography Prints Business Card Design

Background info: Nature, flower, landscape,  macro, wildlife photographer. Shoot color and B&W images. Sell prints at juried fine art shows.
Looking for two-sided, clean, memorable design with creative use of my initials, DK.   I like the DK symbol in the my logo. Just use the DK symbol. Do not leave the underlying text as uploaded by me. I do not like the serif font and positioning of the words!  Either  remove the small print "Dorian Kessler Photography" under the logo,  or change to a sans serif font, or reposition with "Dorian Kessler" above "Photography" which seems to work with serif fonts.
Target Market(s)
Sophisticated art buyers, post-college to middle age
Industry/Entity Type
Business
Contact Information for Business Card
Dorian Kessler Photography
842 Harrow Bend CT
Ashbury Falls, NC 27390
(336) 555-0148
www.doriankessler.com
PW:kesslerphoto
dorian@doriankessler.com
If using just one line address, make sure there is a comma after  "CT" in street address. For example:
842 Harrow Bend CT, Ashbury Falls, NC 27390
Requirements
Must have
- 1.Two-sided card submitted as one design.
2. Must use the DK symbol in my logo.
3. Do not leave the text "Dorian Kessler Photography" under the DK symbol in the logo uploaded by me. I do not like that serif font or the positioning of the words! Either remove the small print "Dorian Kessler Photography" under the logo entirely, or change text to a sans serif font, or reposition text with "Dorian Kessler" above "Photography" which seems to work with serif fonts.
Nice to have
- Can use my DK logo (three file types uploaded: AI, PSD, TIF)  I  like the attached B&W water droplet photo.  My pictures on my website, www.doriankkessler.com  can also be used.  Possible use of Pinwave logo with (either the "f" alone or the square blue icon with white "f") my PW page short url name: kesslerphoto.
Should not have
- 1.No icons or pictures  of camera or lenses or other photographic gear or film strips.
2. No QR or other "barcode" type symbols.
3. No outlining of my logo symbol (drop shadow possibly).
4. No decorative or outlined fonts.
5. I am not a fan of most script fonts.
6. No play on "Kessler" such as snow or other winter season symbols.
7. Do not keep the original text, "Dorian Kessler Photography" under DK logo. Change it or remove it entirely.

```html
<!DOCTYPE html>
<html lang="en">
<head>
<meta charset="utf-8">
<title>Dorian Kessler Photography – Business Card</title>
<link rel="stylesheet" href="https://fonts.googleapis.com/css2?family=Saira:wght@400;500;600&display=swap">
<style>
  :root {
    --backdrop: #c9cacc;
    --card-black: #0c0c0c;
    --card-charcoal: #1c1c1c;
    --brand-green: #7cc242;
    --text-white: #f2f2f2;
    --photo-gray-light: #9a9a9a;
    --photo-gray-dark: #2a2a2a;
  }
  * { box-sizing: border-box; margin: 0; padding: 0; }
  html, body {
    width: 1200px; height: 900px; overflow: hidden;
    background: radial-gradient(ellipse at 40% 30%, #dcdde0 0%, var(--backdrop) 70%);
    font-family: "Saira", "Arial", sans-serif;
  }
  .card {
    position: absolute;
    width: 560px; height: 320px;
    border-radius: 22px;
    overflow: hidden;
    background: radial-gradient(ellipse at 70% 30%, var(--card-charcoal) 0%, var(--card-black) 75%);
    box-shadow: 0 10px 24px rgba(0,0,0,0.35);
  }
  .card--front { left: 90px; top: 90px; }
  .card--back { left: 550px; top: 480px; }

  /* Front */
  .front-photo {
    position: absolute; left: 0; top: 0; width: 330px; height: 320px;
    background:
      radial-gradient(ellipse 32% 24% at 62% 42%, #8fd63f 0%, #5aa52c 60%, transparent 100%),
      radial-gradient(ellipse 55% 45% at 38% 78%, #e2461c 0%, #d8782a 40%, #b3a02d 70%, transparent 100%);
  }
  .monogram {
    position: absolute; color: var(--brand-green);
    font-weight: 500; letter-spacing: 2px; line-height: 1;
  }
  .card--front .monogram { right: 30px; top: 38px; font-size: 84px; }
  .front-name {
    position: absolute; right: 96px; top: 132px; text-align: right;
    color: var(--brand-green);
  }
  .front-name .name {
    font-size: 24px; font-weight: 500; letter-spacing: 1px; text-transform: uppercase; line-height: 1;
  }
  .front-name .trade {
    font-size: 11px; letter-spacing: 2px; text-transform: uppercase; margin-top: 3px;
  }

  /* Back */
  .back-photo {
    position: absolute; left: 0; top: 0; width: 360px; height: 320px;
    background:
      radial-gradient(ellipse 60% 50% at 40% 45%, var(--photo-gray-light) 0%, #5a5a5a 45%, var(--photo-gray-dark) 80%, transparent 100%);
  }
  .card--back .monogram { right: 110px; top: 24px; font-size: 80px; }
  .contact {
    position: absolute; right: 28px; top: 132px; text-align: right;
    color: var(--text-white); font-size: 13px; line-height: 1.3;
    text-transform: uppercase; letter-spacing: 0.5px;
  }
  .contact .business { color: var(--brand-green); font-weight: 600; font-size: 14px; }
  .contact-row { display: flex; justify-content: flex-end; align-items: center; gap: 6px; }
  .icon { width: 12px; height: 12px; flex: none; }
  .bottom-lines {
    position: absolute; left: 28px; bottom: 26px;
    color: var(--text-white); font-size: 14px; line-height: 1.3; text-transform: uppercase;
  }
  .bottom-lines .web { color: var(--brand-green); font-weight: 600; font-size: 16px; }
  .bottom-lines .contact-row { justify-content: flex-start; gap: 14px; }
  .bottom-lines .pair { display: flex; align-items: center; gap: 6px; }
  .pinwave-mark { width: 11px; height: 11px; background: var(--brand-green); border-radius: 2px; flex: none; }
</style>
</head>
<body>
  <section class="card card--front">
    <div class="front-photo" role="img" aria-label="Photograph of a bright green tree frog with red eyes perched on a red and orange tropical flower"></div>
    <div class="monogram">DK</div>
    <div class="front-name">
      <div class="name">Dorian Kessler</div>
      <div class="trade">Photography</div>
    </div>
  </section>

  <section class="card card--back">
    <div class="back-photo" role="img" aria-label="Black and white close-up photograph of a tortoise eye and wrinkled skin"></div>
    <div class="monogram">DK</div>
    <div class="contact">
      <div class="business">Dorian Kessler Photography</div>
      <div>842 Harrow Bend CT</div>
      <div>Ashbury Falls, NC 27390</div>
      <div>www.doriankessler.com</div>
      <div class="contact-row"><span class="pinwave-mark"></span><span>kesslerphoto</span></div>
    </div>
    <div class="bottom-lines">
      <div class="contact-row">
        <span class="pair">
          <svg class="icon" viewBox="0 0 12 12" aria-hidden="true"><rect width="12" height="12" rx="2" fill="#7cc242"/><path d="M3.4 2.6c.4-.3.8-.2 1 .2l.7 1.2c.2.4.1.7-.2 1l-.4.3c.4.9 1 1.5 1.9 1.9l.3-.4c.3-.3.6-.4 1-.2l1.2.7c.4.2.5.6.2 1l-.5.6c-.4.4-1 .5-1.6.2C5.3 8.4 3.6 6.7 2.9 4.9c-.3-.6-.2-1.2.2-1.6z" fill="#0c0c0c"/></svg>
          <span>336-555-0148</span>
        </span>
        <span class="pair">
          <svg class="icon" viewBox="0 0 12 12" aria-hidden="true"><rect width="12" height="12" rx="2" fill="#7cc242"/><rect x="2.2" y="3.4" width="7.6" height="5.2" fill="none" stroke="#0c0c0c" stroke-width="1"/><path d="M2.4 3.6 6 6.4l3.6-2.8" fill="none" stroke="#0c0c0c" stroke-width="1"/></svg>
          <span>dorian@doriankessler.com</span>
        </span>
      </div>
      <div class="web">www.doriankessler.com</div>
    </div>
  </section>
</body>
</html>
```